Brookfarrow Osteopathy and dry needling business card

Business card for Brookfarrow Osteopathy and Dry Needling.

Industry/Entity Type

Health

Contact Information for Business Card

I do not have a phone number yet. I also do not have an email address yet. The physical address is: 48 Lower Crane Street Brookfarrow The website is: www.brookfarrowosteosteopathy.example My details are: Dr Martin Pellowe, Osteopath (B.Clin.Sci (Ost) M.Ost BSC ECON (Hons)

Colors
0094D4
00A9DD
6FCCEA
C7EBF8
E9F6FB

Requirements
Must have
• logo on the back
Nice to have
• Maybe a space for me to write an appointment time and date on the card.

```html
<!DOCTYPE html>
<html lang="en">
<head>
<meta charset="utf-8">
<title>Brookfarrow Osteopathy and Dry Needling – Business Card</title>
<link href="https://fonts.googleapis.com/css2?family=Montserrat:wght@400;700&family=Roboto:wght@400;500&display=swap" rel="stylesheet">
<style>
  :root {
    --backdrop: #b9b9b9;
    --card: #f3f3f2;
    --blue: #0a82c6;
    --blue-deep: #0094d4;
    --orange: #e8821e;
    --ink: #4a4a4a;
  }
  * { box-sizing: border-box; margin: 0; padding: 0; }
  html, body { width: 1200px; height: 945px; overflow: hidden; }
  body {
    background: var(--backdrop);
    display: flex;
    flex-direction: column;
    align-items: center;
    justify-content: center;
    gap: 45px;
    font-family: "Roboto", Arial, sans-serif;
  }
  .card {
    position: relative;
    width: 700px;
    height: 400px;
    background: var(--card);
    box-shadow: 0 8px 24px rgba(0,0,0,0.18);
  }
  /* Front */
  .holder {
    position: absolute;
    top: 52px;
    right: 48px;
    text-align: right;
  }
  .holder-name {
    font-family: "Montserrat", Arial, sans-serif;
    font-weight: 700;
    font-size: 38px;
    color: var(--blue);
    letter-spacing: -0.5px;
  }
  .holder-name .title { font-weight: 400; }
  .holder-credentials {
    font-size: 14px;
    font-weight: 500;
    color: var(--orange);
    margin-top: 2px;
  }
  .brand {
    position: absolute;
    left: 48px;
    top: 150px;
    display: flex;
    align-items: center;
    gap: 12px;
    width: 230px;
  }
  .brand-dot {
    flex: none;
    width: 28px;
    height: 28px;
    border-radius: 50%;
    background: var(--blue-deep);
  }
  .brand-name {
    font-size: 17px;
    font-weight: 500;
    color: var(--blue);
    line-height: 1.25;
  }
  .spine-art {
    position: absolute;
    right: 0;
    top: 150px;
    width: 300px;
    height: 170px;
  }
  .contact {
    position: absolute;
    left: 48px;
    bottom: 42px;
    list-style: none;
    font-size: 19px;
    color: var(--ink);
  }
  .contact li {
    display: flex;
    align-items: center;
    gap: 10px;
    margin-top: 8px;
  }
  .contact svg { width: 20px; height: 20px; flex: none; }
  /* Back */
  .card-back {
    display: flex;
    align-items: center;
    justify-content: center;
  }
  .card-back .brand {
    position: static;
    width: 320px;
  }
  .card-back .brand-name { font-size: 22px; }
  .card-back .brand-dot { width: 36px; height: 36px; }
</style>
</head>
<body>
  <section class="card card-front">
    <div class="holder">
      <p class="holder-name"><span class="title">Dr</span> Martin Pellowe</p>
      <p class="holder-credentials">Osteopath (B.Clin.Sci (Ost) M.Ost BSC ECON (Hons)</p>
    </div>

    <div class="brand">
      <span class="brand-dot"></span>
      <span class="brand-name">Brookfarrow Osteopathy and Dry Needling</span>
    </div>

    <svg class="spine-art" viewBox="0 0 300 170" role="img" aria-label="Illustration of a curving blue spine">
      <path d="M0 170 C60 120 120 70 300 20 L300 0 C120 45 50 100 0 160 Z" fill="var(--blue-deep)"/>
    </svg>

    <ul class="contact">
      <li>
        <svg viewBox="0 0 24 24" aria-hidden="true"><path d="M12 2a7 7 0 0 0-7 7c0 5 7 13 7 13s7-8 7-13a7 7 0 0 0-7-7zm0 9.5A2.5 2.5 0 1 1 12 6.5a2.5 2.5 0 0 1 0 5z" fill="var(--blue)"/></svg>
        48 Lower Crane Street Brookfarrow
      </li>
      <li>
        <svg viewBox="0 0 24 24" aria-hidden="true"><circle cx="12" cy="12" r="9" fill="none" stroke="var(--blue)" stroke-width="2.2"/><path d="M3 12h18M12 3c3 3 3 15 0 18M12 3c-3 3-3 15 0 18" fill="none" stroke="var(--blue)" stroke-width="1.8"/></svg>
        www.brookfarrowosteosteopathy.example
      </li>
    </ul>
  </section>

  <section class="card card-back">
    <div class="brand">
      <span class="brand-dot"></span>
      <span class="brand-name">Brookfarrow Osteopathy and Dry Needling</span>
    </div>
  </section>
</body>
</html>
```